Personal informs intake and New Zealand divorce form automated filling service

I need a website that has a professional appearance, take information from clients, automatically fill New Zealand divorce forms based on information gathered. The personal information are listed:
Applicant’s information

1 First name

2 Middle name ( if Any )

3 Last name

4 Date of birth

5 Address

6 Email

7 Gender

8 Mobile

9 Occupation

10 Ethnicity

11 Country of residence

12 Do you live in New Zealand permanently?

13 Do you and your spouse have children who are under age 16 who require additional care?

Spouse’s information

1 Spouse’s first name

2 Spouse’s middle name ( if any )

3 Spouse’s last name

4 Spouse’s date of birth

5 Spouse’s occupation

6 Spouse’s ethnicity

7 Mobil number

8 Address

Marriage details

1 Did either party change their name by deed poll following the marriage/ civil union.

2 Date of marriage

3 Place and Address where the marriage was solemnized?

4 What date did you start living together?

5 What date did you cease living together?

6 How did you agree to separate? ( verbal agreement, written agreement, court order, or other )

The forms are New Zealand one party/joint application for Order dissolving a marriage or civil union.
Once the forms are completed, it will be checked by a human before sending to the paid clients by email. The website needs to integrate multiple mainstream payment options.

The forms are uploaded, please view it and set up the questionnaire accordingly to ensure all questions in the forms are answered. Must be able to distinguish one party or joint application.

Please contact me if you are interested and need more information.

Updated an AI generated draft as a sample

Target Market(s)

Divorcées

Coding

Coded - Design and coding required

Number of Pages Required

1 page

Font styles to use
Sans Serif

Colors

Designer to choose colors to be used in the design.

Requirements
Must have
• A professional appearance, easy to initiate the information intake process
Nice to have
• Step by step guideline, easy to understand how the website works
Should not have
• Bright colors

```html
<!DOCTYPE html>
<html lang="en">
<head>
<meta charset="UTF-8">
<title>New Zealand Divorce Application</title>
<link href="https://fonts.googleapis.com/css2?family=Arimo:wght@400;700&display=swap" rel="stylesheet">
<style>
  :root {
    --backdrop: #5a5a5a;
    --page-bg: #f1f2f4;
    --card-bg: #ffffff;
    --ink: #1f2329;
    --muted: #555b63;
    --field-border: #c9ced5;
    --accent: #0b56a8;
    --accent-line: #8fb3dd;
    --footer-bg: #083d86;
    --hero-dark: #3b3f46;
    --hero-light: #d9d6d0;
    --white: #ffffff;
  }
  * { box-sizing: border-box; margin: 0; padding: 0; }
  html, body { width: 1200px; height: 2669px; overflow: hidden; }
  body {
    background: var(--backdrop);
    font-family: "Arimo", Arial, sans-serif;
    color: var(--ink);
  }
  .page {
    position: absolute;
    left: 72px; top: 72px;
    width: 1056px;
    background: var(--page-bg);
  }
  .hero {
    position: relative;
    height: 560px;
    background: linear-gradient(120deg, var(--hero-light) 0%, #b9b4ac 35%, #6f7680 60%, var(--hero-dark) 100%);
    display: flex; flex-direction: column; align-items: center; justify-content: center;
    text-align: center;
  }
  .hero-shade { position: absolute; inset: 0; background: rgba(20, 24, 30, 0.28); }
  .hero-title, .hero-subtitle { position: relative; color: var(--white); }
  .hero-title { font-size: 32px; font-weight: 700; }
  .hero-subtitle { font-size: 16px; margin-top: 14px; }
  .form-card {
    width: 816px;
    margin: 10px auto 0;
    background: var(--card-bg);
    padding: 44px 28px 28px;
  }
  .section-title {
    font-size: 22px; font-weight: 700;
    padding-bottom: 6px;
    border-bottom: 3px solid var(--accent-line);
    margin-bottom: 10px;
  }
  .section + .section { margin-top: 26px; }
  .field { height: 53px; }
  .field-wide { height: 58px; }
  .field-label { display: block; font-size: 13px; font-weight: 700; line-height: 16px; margin-bottom: 4px; }
  .field-input {
    height: 28px;
    border: 1px solid var(--field-border);
    border-radius: 3px;
    padding: 0 8px;
    font-size: 12px; color: var(--muted);
    display: flex; align-items: center; justify-content: space-between;
  }
  .field-input svg { width: 12px; height: 12px; }
  .submit-button {
    display: inline-block;
    margin-top: 24px;
    background: var(--accent); color: var(--white);
    font-size: 13px; font-weight: 700;
    padding: 9px 16px; border-radius: 3px;
  }
  .site-footer {
    margin-top: 32px;
    height: 112px;
    background: var(--footer-bg);
    color: var(--white);
    font-size: 13px; line-height: 19px;
    text-align: center;
    padding-top: 27px;
  }
</style>
</head>
<body>
<div class="page">
  <header class="hero" role="img" aria-label="Photograph of a couple in a tense discussion on a sofa">
    <div class="hero-shade"></div>
    <h1 class="hero-title">New Zealand Divorce Application</h1>
    <p class="hero-subtitle">Begin your separation process with confidence and ease</p>
  </header>

  <main class="form-card">
    <section class="section">
      <h2 class="section-title">Applicant's Information</h2>
      <div class="field"><span class="field-label">First Name</span><div class="field-input"></div></div>
      <div class="field"><span class="field-label">Middle Name</span><div class="field-input"></div></div>
      <div class="field"><span class="field-label">Last Name</span><div class="field-input"></div></div>
      <div class="field"><span class="field-label">Date of Birth</span><div class="field-input">dd/mm/yyyy<svg viewBox="0 0 12 12"><rect x="1" y="2" width="10" height="9" fill="none" stroke="#333"/><line x1="1" y1="5" x2="11" y2="5" stroke="#333"/></svg></div></div>
      <div class="field"><span class="field-label">Address</span><div class="field-input"></div></div>
      <div class="field"><span class="field-label">Email</span><div class="field-input"></div></div>
      <div class="field"><span class="field-label">Gender</span><div class="field-input">Male<svg viewBox="0 0 12 12"><path d="M2 4l4 4 4-4" fill="none" stroke="#333"/></svg></div></div>
      <div class="field"><span class="field-label">Mobile</span><div class="field-input"></div></div>
      <div class="field"><span class="field-label">Occupation</span><div class="field-input"></div></div>
      <div class="field"><span class="field-label">Ethnicity</span><div class="field-input"></div></div>
      <div class="field"><span class="field-label">Country of Residence</span><div class="field-input"></div></div>
      <div class="field"><span class="field-label">Live in NZ permanently?</span><div class="field-input">Yes<svg viewBox="0 0 12 12"><path d="M2 4l4 4 4-4" fill="none" stroke="#333"/></svg></div></div>
      <div class="field"><span class="field-label">Children under 16 needing care?</span><div class="field-input">Yes<svg viewBox="0 0 12 12"><path d="M2 4l4 4 4-4" fill="none" stroke="#333"/></svg></div></div>
    </section>

    <section class="section">
      <h2 class="section-title">Spouse's Information</h2>
      <div class="field"><span class="field-label">First Name</span><div class="field-input"></div></div>
      <div class="field"><span class="field-label">Middle Name</span><div class="field-input"></div></div>
      <div class="field"><span class="field-label">Last Name</span><div class="field-input"></div></div>
      <div class="field"><span class="field-label">Date of Birth</span><div class="field-input">dd/mm/yyyy<svg viewBox="0 0 12 12"><rect x="1" y="2" width="10" height="9" fill="none" stroke="#333"/><line x1="1" y1="5" x2="11" y2="5" stroke="#333"/></svg></div></div>
      <div class="field"><span class="field-label">Occupation</span><div class="field-input"></div></div>
      <div class="field"><span class="field-label">Ethnicity</span><div class="field-input"></div></div>
      <div class="field"><span class="field-label">Mobile</span><div class="field-input"></div></div>
      <div class="field"><span class="field-label">Address</span><div class="field-input"></div></div>
    </section>

    <section class="section">
      <h2 class="section-title">Marriage Details</h2>
      <div class="field-wide"><span class="field-label">Name change after marriage?</span><div class="field-input">Yes<svg viewBox="0 0 12 12"><path d="M2 4l4 4 4-4" fill="none" stroke="#333"/></svg></div></div>
      <div class="field-wide"><span class="field-label">Date of Marriage</span><div class="field-input">dd/mm/yyyy<svg viewBox="0 0 12 12"><rect x="1" y="2" width="10" height="9" fill="none" stroke="#333"/><line x1="1" y1="5" x2="11" y2="5" stroke="#333"/></svg></div></div>
      <div class="field-wide"><span class="field-label">Place of Marriage</span><div class="field-input"></div></div>
      <div class="field-wide"><span class="field-label">Date started living together</span><div class="field-input">dd/mm/yyyy<svg viewBox="0 0 12 12"><rect x="1" y="2" width="10" height="9" fill="none" stroke="#333"/><line x1="1" y1="5" x2="11" y2="5" stroke="#333"/></svg></div></div>
      <div class="field-wide"><span class="field-label">Date separated</span><div class="field-input">dd/mm/yyyy<svg viewBox="0 0 12 12"><rect x="1" y="2" width="10" height="9" fill="none" stroke="#333"/><line x1="1" y1="5" x2="11" y2="5" stroke="#333"/></svg></div></div>
      <div class="field-wide"><span class="field-label">How did you agree to separate?</span><div class="field-input">Verbal Agreement<svg viewBox="0 0 12 12"><path d="M2 4l4 4 4-4" fill="none" stroke="#333"/></svg></div></div>
    </section>

    <span class="submit-button">Submit Application</span>
  </main>

  <footer class="site-footer">
    <p>© 2025 Your Legal Service Name. All rights reserved.</p>
    <p>This website does not provide legal advice. Submissions are reviewed manually before processing.</p>
    <p>Privacy Policy | Terms of Use</p>
  </footer>
</div>
</body>
</html>
```